Prestige Car Bodyshop Business Card

We are a car bodyshop based in the UK. Our customer base is mainly prestige high-value vehicles. I am looking for a classy and stylish business card design for my staff to give out to customers, with their direct email and phone number, as well as our main email and phone number with address details

I am also looking to have a general business card design with just our main company address and contact details, but also have a space to add a manufacturer approval logo (i.e Velmora, Orek, Tovalo etc... logo) in the corner somewhere.

I do not particularly want any outlines or pictures of cars on the card, I would just like a quality high-end look.

Please feel free to get in touch if you have any questions or queries?

Many Thanks

Malcolm

Target Market(s)

Prestige vehicle owners

Industry/Entity Type

Automotive

Contact Information for Business Card

I am looking for a classy and stylish business card design for my staff to give out to customers, with their direct email and phone number, as well as our main email and phone number with address details

Font styles to use
Sans Serif

Colors

Designer to choose colors to be used in the design.

Requirements
Nice to have
• I do not particularly want any outlines or pictures of cars on the card, I would just like a quality high-end look.

```html
<!DOCTYPE html>
<html lang="en">
<head>
<meta charset="utf-8">
<title>Halvern Business Cards</title>
<link rel="stylesheet" href="https://fonts.googleapis.com/css2?family=Josefin+Sans:wght@600&family=Open+Sans:wght@400&display=swap">
<style>
  :root {
    --backdrop: #636363;
    --paper: #ffffff;
    --navy: #23356b;
    --orange: #f2a66a;
    --trim: #e0553f;
    --frame: #1e2233;
    --ink: #222634;
    --link-blue: #2a4f9a;
  }
  * { margin: 0; padding: 0; box-sizing: border-box; }
  html, body { width: 840px; height: 1200px; overflow: hidden; background: var(--backdrop); }
  .canvas { position: relative; width: 840px; height: 1200px; }

  .card {
    position: absolute; left: 80px; width: 684px; height: 418px;
    outline: 1.5px solid var(--trim); overflow: hidden;
  }
  .card--front { top: 149px; background: var(--paper); }
  .card--back { top: 624px; background: var(--orange); }

  .card__shapes { position: absolute; inset: 0; }
  .card__frame { position: absolute; left: 24px; top: 23px; width: 639px; height: 374px; border: 1px solid var(--frame); }
  .card--back .card__frame { top: 24px; height: 373px; border-color: #8a8078; }

  .company {
    position: absolute; font-family: "Open Sans", sans-serif; font-weight: 400;
    color: var(--navy); line-height: 1.25;
  }
  .card--front .company { left: 84px; top: 178px; width: 250px; font-size: 20px; }
  .card--back .company { left: 0; right: 0; top: 160px; text-align: center; font-size: 34px; }

  .divider { position: absolute; left: 345px; top: 154px; width: 3px; height: 112px; background: var(--navy); }

  .person { position: absolute; left: 358px; top: 144px; font-family: "Open Sans", sans-serif; color: var(--ink); }
  .person__name { font-size: 28px; line-height: 1; margin-bottom: 15px; }
  .person__line { display: flex; align-items: center; font-size: 15.5px; height: 24px; }
  .person__line svg { width: 14px; height: 14px; margin: 0 10px 0 3px; fill: var(--ink); }

  .website {
    position: absolute; left: 0; right: 0; text-align: center;
    font-family: "Josefin Sans", sans-serif; font-weight: 600; font-size: 16px; letter-spacing: .3px;
  }
  .card--front .website { top: 343px; color: var(--ink); }
  .card--back .website { top: 360px; color: var(--link-blue); }
</style>
</head>
<body>
<main class="canvas">

  <section class="card card--front">
    <svg class="card__shapes" viewBox="0 0 684 418" aria-hidden="true">
      <path d="M0 208 C 40 330 150 400 268 418 L0 418 Z" fill="var(--orange)"/>
      <path d="M436 0 C 560 40 650 120 684 211 L684 0 Z" fill="var(--navy)"/>
    </svg>
    <div class="card__frame"></div>

    <p class="company">Halvern<br>Accident Repair Centre</p>

    <div class="divider"></div>

    <div class="person">
      <p class="person__name">Your Name</p>
      <p class="person__line">
        <svg viewBox="0 0 24 24"><path d="M12 2a7 7 0 0 0-7 7c0 5 7 13 7 13s7-8 7-13a7 7 0 0 0-7-7zm0 9.5A2.5 2.5 0 1 1 12 6.5a2.5 2.5 0 0 1 0 5z"/></svg>
        Your Local
      </p>
      <p class="person__line">
        <svg viewBox="0 0 24 24"><path d="M6.6 10.8a15 15 0 0 0 6.6 6.6l2.2-2.2a1 1 0 0 1 1-.25 11.4 11.4 0 0 0 3.6.57 1 1 0 0 1 1 1V20a1 1 0 0 1-1 1A17 17 0 0 1 3 4a1 1 0 0 1 1-1h3.5a1 1 0 0 1 1 1c0 1.25.2 2.45.57 3.57a1 1 0 0 1-.25 1z"/></svg>
        Your Phone
      </p>
      <p class="person__line">
        <svg viewBox="0 0 24 24"><path d="M3 5h18v14H3z" fill="var(--ink)"/><path d="M4 6.5l8 6 8-6" stroke="#fff" stroke-width="1.6" fill="none"/></svg>
        Your Email
      </p>
    </div>

    <p class="website">WWW.YOURSITE.COM</p>
  </section>

  <section class="card card--back">
    <div class="card__frame"></div>
    <p class="company">Halvern<br>Accident Repair Centre</p>
    <p class="website">WWW.YOURSITE.COM</p>
  </section>

</main>
</body>
</html>
```